Brantwell Group needs a business card design

We need a new business card design using the logo recently selected in a logo competition on Pixel Forum. Our business is a consultancy specializing in aviation and energy and the winning business card design will promote an image of precision and professionalism with creativity.

Please use the logo with the name on the front of the card and use a complementary font. Make the back white with either the light grey or dark grey logo.

Target Market(s)

Senior finance and legal leaders at aviation and energy companies

Industry/Entity Type

Management Consulting

Contact Information for Business Card

Peter Haldane
President
Brantwell Group

www.brantwellgroup.example

(555) 304-6198
ph@brantwellgroup.example

Requirements
Must have
• Professional font that goes well with the logo font

```html
<!DOCTYPE html>
<html lang="en">
<head>
<meta charset="utf-8">
<title>Brantwell Group — Business Card</title>
<link rel="stylesheet" href="https://fonts.googleapis.com/css2?family=Roboto:wght@300;400;500;700&display=swap">
<style>
  :root {
    --backdrop: #d3d6d6;
    --card-stock: #e4e2ea;
    --ink-grey: #55565c;
    --ink-dark: #3f4044;
    --ink-navy: #1f2a6b;
    --ink-blue: #2d4a9a;
    --edge-navy: #1a1f6e;
  }
  * { box-sizing: border-box; margin: 0; padding: 0; }
  html, body {
    width: 1200px;
    height: 1050px;
    overflow: hidden;
    background: var(--backdrop);
    font-family: "Roboto", Arial, sans-serif;
  }
  .sheet {
    width: 1200px;
    height: 1050px;
    display: flex;
    flex-direction: column;
    align-items: center;
    justify-content: center;
    gap: 60px;
  }
  .card {
    position: relative;
    width: 700px;
    height: 400px;
    background: var(--card-stock);
    border-bottom: 6px solid var(--edge-navy);
    box-shadow: 0 14px 30px rgba(0, 0, 0, 0.12);
  }

  /* Front */
  .card-front { padding: 44px 52px; }
  .holder-name {
    font-size: 30px;
    font-weight: 400;
    color: var(--ink-grey);
    letter-spacing: 0.5px;
  }
  .holder-title {
    margin-top: 4px;
    font-size: 15px;
    font-weight: 700;
    color: var(--ink-blue);
    letter-spacing: 2.5px;
  }
  .contact-list {
    list-style: none;
    margin-top: 30px;
    font-size: 17px;
    color: var(--ink-grey);
  }
  .contact-list li { display: flex; gap: 22px; line-height: 28px; }
  .contact-label {
    width: 14px;
    font-weight: 500;
    color: var(--ink-navy);
  }
  .brand-lockup {
    position: absolute;
    right: 52px;
    top: 170px;
    display: flex;
    align-items: center;
    gap: 10px;
    font-size: 20px;
    font-weight: 400;
    letter-spacing: 3px;
    color: var(--ink-navy);
    text-transform: uppercase;
  }
  .brand-square {
    width: 16px;
    height: 16px;
    background: var(--ink-navy);
  }
  .service-band {
    position: absolute;
    left: 52px;
    right: 52px;
    bottom: 40px;
  }
  .service-rule {
    height: 5px;
    background: var(--ink-navy);
    margin-bottom: 12px;
  }
  .service-line {
    font-size: 19px;
    font-weight: 500;
    letter-spacing: 3.6px;
    color: var(--ink-navy);
    line-height: 28px;
    white-space: nowrap;
  }

  /* Back */
  .card-back {
    display: flex;
    align-items: center;
    justify-content: center;
  }
  .back-mark {
    font-size: 46px;
    font-weight: 400;
    letter-spacing: 6px;
    color: var(--ink-dark);
    text-transform: uppercase;
  }
</style>
</head>
<body>
  <main class="sheet">
    <section class="card card-front" aria-label="Business card front">
      <h1 class="holder-name">Peter Haldane</h1>
      <p class="holder-title">PRESIDENT</p>
      <ul class="contact-list">
        <li><span class="contact-label">T</span><span>(555) 304-6198</span></li>
        <li><span class="contact-label">E</span><span>ph@brantwellgroup.example</span></li>
        <li><span class="contact-label">W</span><span>www.brantwellgroup.example</span></li>
      </ul>
      <div class="brand-lockup">
        <span class="brand-square"></span>
        <span>Brantwell Group</span>
      </div>
      <div class="service-band">
        <div class="service-rule"></div>
        <p class="service-line">FINANCE AND STRATEGY CONSULTING</p>
        <p class="service-line">AVIATION - MANUFACTURING - ENERGY</p>
      </div>
    </section>

    <section class="card card-back" aria-label="Business card back">
      <p class="back-mark">Brantwell Group</p>
    </section>
  </main>
</body>
</html>
```